Ironleaf Personal Training Studio Information Card

The front and back of card to give people that walk in to our gym. There are a few things to say on the card. But it also needs to be designed in an attractive way. You can make some of the information bullett points or with icons or graphics. Please look at our website at https://ironleaftraining.com/ . The card will be 4" x 9"

Target Market(s)

High End Clientele who want to train in a private gym

Industry/Entity Type

Fitness

Font styles to use
Serif
Sans Serif
Other font styles liked:
• the same font Velto uses on the zelpad

Colors
F0912C
F2A743
F7CA91
FBE8D2
FDF5EE

Requirements
Must have
• A cool look

```html
<!DOCTYPE html>
<html lang="en">
<head>
<meta charset="utf-8">
<title>Ironleaf Private Training Studio – Rack Card</title>
<link rel="stylesheet" href="https://fonts.googleapis.com/css2?family=League+Spartan:wght@500;600;700&family=Montserrat:wght@400;500;600;700&display=swap">
<style>
:root{
  --stage:#c0c0c0;
  --paper:#ffffff;
  --red:#e8313a;
  --ink:#2b2b2b;
  --soft:#e9eaec;
  --photo-blue-1:#2d4a70;
  --photo-blue-2:#0f1a2b;
  --photo-dark-1:#3a3a42;
  --photo-dark-2:#101014;
}
*{box-sizing:border-box;margin:0;padding:0}
html,body{width:1200px;height:1200px;overflow:hidden;background:var(--stage)}
body{position:relative;font-family:"Montserrat",sans-serif;color:var(--ink)}
.card{position:absolute;top:211px;width:360px;height:810px;background:var(--paper);overflow:hidden}
.card--front{left:181px}
.card--back{left:661px}
.card > *{position:absolute}
.art{left:0;top:0;width:360px;height:360px}
.band{left:0;width:360px;background:var(--soft)}
.brand{left:25px;top:26px;line-height:1}
.brand__name{font-family:"League Spartan",sans-serif;font-weight:700;font-size:30px;letter-spacing:.5px;color:#555;display:flex;align-items:center;gap:7px}
.brand__mark{width:12px;height:12px;background:var(--red);display:inline-block}
.brand__tag{font-family:"Montserrat",sans-serif;font-weight:600;font-size:7.6px;letter-spacing:3px;margin-top:7px;color:#555}
.card--back .brand__name,.card--back .brand__tag{color:#fff}
.headline{left:22px;top:327px;font-family:"League Spartan",sans-serif;font-weight:600;font-size:24.5px;line-height:26.3px;letter-spacing:.6px;text-transform:uppercase}
.accent{color:var(--red)}
.rule{left:22px;width:131px;height:2px;background:var(--red)}
.body-copy{left:22px;width:320px;font-size:9.7px;line-height:12px;letter-spacing:.25px;color:#3a3a3a}
.tag{left:22px;width:131px;height:25px;background:var(--red);color:#fff;font-family:"League Spartan",sans-serif;font-weight:600;font-size:13.5px;letter-spacing:.8px;text-transform:uppercase;display:flex;align-items:center;padding-left:10px;padding-top:2px}
.goal{display:flex;flex-direction:column;gap:7px;font-size:10.3px;letter-spacing:.2px}
.goal svg{width:17px;height:17px}
.contact-line{left:0;top:698px;width:360px;height:2px;background:var(--red)}
.contact-tag{left:22px;top:686px;width:131px;height:25px;background:#fff;border:2px solid var(--red);font-family:"League Spartan",sans-serif;font-weight:600;font-size:13.5px;letter-spacing:.9px;display:flex;align-items:center;justify-content:center;padding-top:2px}
.contact{left:22px;display:flex;align-items:center;gap:8px;font-size:10.3px;letter-spacing:.9px}
.contact svg{width:18px;height:17px}
.contact--phone{font-family:"League Spartan",sans-serif;font-weight:700;font-size:14.5px;letter-spacing:.6px;padding-top:0}
.section-title{left:22px;top:308px;font-family:"League Spartan",sans-serif;font-weight:600;font-size:16px;letter-spacing:.7px;color:var(--red)}
.rates{left:22px;top:494px;font-size:13px;letter-spacing:.3px;font-weight:500}
.rates li{list-style:none;display:flex;height:17.5px;align-items:center}
.rates li::before{content:"";border-left:4px solid var(--ink);border-top:3px solid transparent;border-bottom:3px solid transparent;margin-right:8px}
.rates .when{color:var(--red);font-weight:400;width:122px}
.rates .lead{margin-bottom:5px}
.rates .lead::before{display:none}
.partner{left:0;top:574px;width:338px;height:28px;background:var(--red);color:#fff;font-weight:500;font-size:13px;letter-spacing:.4px;display:flex;align-items:center;padding-left:22px}
.example{left:22px;top:610px;font-size:12px;letter-spacing:.3px;line-height:13.6px}
.example .lead{font-weight:500;font-size:13px;margin-bottom:4px}
.example .row{display:flex}
.example .row span:first-child{color:var(--red);margin-right:7px}
.example .row span:last-child{font-weight:500}
</style>
</head>
<body>

<!-- FRONT -->
<section class="card card--front">
  <svg class="art" viewBox="0 0 360 360" role="img" aria-label="Photo of an athlete doing a dumbbell row from a plank in a dimly lit gym">
    <defs>
      <linearGradient id="gymBlue" x1="0" y1="0" x2="1" y2="1">
        <stop offset="0" stop-color="var(--photo-blue-1)"/>
        <stop offset="1" stop-color="var(--photo-blue-2)"/>
      </linearGradient>
    </defs>
    <polygon points="0,71 74,109 360,61 360,343 74,291 0,333" fill="url(#gymBlue)"/>
    <polygon points="0,69 74,106 360,59 360,63 74,112 0,73" fill="var(--red)"/>
    <polygon points="0,331 74,290 360,340 360,347 74,296 0,339" fill="var(--red)"/>
  </svg>

  <div class="brand">
    <div class="brand__name"><span class="brand__mark"></span>IRONLEAF</div>
    <div class="brand__tag">PRIVATE TRAINING STUDIO</div>
  </div>

  <h1 class="headline">A safe and<br><span class="accent">individualized</span><br>approach <span class="accent">to</span><br><span class="accent">strength</span> training.</h1>
  <div class="rule" style="top:439px"></div>
  <p class="body-copy" style="top:452px">Some ways of training increase the chance of injury, we do not practice those types of training at Ironleaf. Many of our clients have current or past injuries that can cause problems. We work with them to not aggravate those injuries or allow them to become an obstacle to their workouts.</p>

  <div class="band" style="top:561px;height:138px"></div>
  <div class="tag" style="top:548px">Clients Goals</div>

  <div class="goal" style="left:22px;top:586px">
    <svg viewBox="0 0 17 17"><rect width="17" height="17" fill="var(--red)"/><rect x="3" y="5" width="2" height="7" fill="#fff"/><rect x="12" y="5" width="2" height="7" fill="#fff"/><rect x="6" y="6.5" width="1.5" height="4" fill="#fff"/><rect x="9.5" y="6.5" width="1.5" height="4" fill="#fff"/><rect x="5" y="8" width="7" height="1" fill="#fff"/></svg>
    <span>Build Strength</span></div>
  <div class="goal" style="left:123px;top:586px">
    <svg viewBox="0 0 17 17"><rect width="17" height="17" fill="var(--red)"/><circle cx="10" cy="4.5" r="1.6" fill="#fff"/><path d="M4 7l5 1 2 5M9 8l-3 5" stroke="#fff" stroke-width="1.6" fill="none" stroke-linecap="round"/></svg>
    <span>Increase Flexibility</span></div>
  <div class="goal" style="left:257px;top:586px">
    <svg viewBox="0 0 17 17"><rect width="17" height="17" fill="var(--red)"/><circle cx="8.5" cy="8.5" r="5" fill="#fff"/><path d="M8.5 8.5l2-2" stroke="var(--red)" stroke-width="1.4"/></svg>
    <span>Weight Loss</span></div>
  <div class="goal" style="left:22px;top:631px">
    <svg viewBox="0 0 17 17"><rect width="17" height="17" fill="var(--red)"/><rect x="4" y="6" width="9" height="7" fill="none" stroke="#fff" stroke-width="1.4"/><rect x="6" y="3.5" width="5" height="2.5" fill="#fff"/></svg>
    <span>Body Sculpting</span></div>
  <div class="goal" style="left:123px;top:631px">
    <svg viewBox="0 0 17 17"><rect width="17" height="17" fill="var(--red)"/><circle cx="9" cy="4.5" r="1.6" fill="#fff"/><path d="M8 7l-2 4h6M4 13h9" stroke="#fff" stroke-width="1.6" fill="none" stroke-linecap="round"/></svg>
    <span>Functional Movement</span></div>
  <div class="goal" style="left:257px;top:631px">
    <svg viewBox="0 0 17 17"><rect width="17" height="17" fill="var(--red)"/><path d="M8.5 13s-4.5-3-4.5-6a2.3 2.3 0 0 1 4.5-1 2.3 2.3 0 0 1 4.5 1c0 3-4.5 6-4.5 6z" fill="#fff"/></svg>
    <span>Improve Health</span></div>

  <div class="contact-line"></div>
  <div class="contact-tag">CONTACT US</div>
  <div class="contact contact--phone" style="top:724px">
    <svg viewBox="0 0 18 17"><rect width="18" height="17" fill="var(--red)"/><path d="M5 4l2.5-.5 1 2.5-1.3 1a6 6 0 0 0 3 3l1-1.3 2.5 1-.5 2.5C9 12.5 5.5 9 5 4z" fill="none" stroke="#fff" stroke-width="1"/></svg>555.014.2290</div>
  <div class="contact" style="top:747px">
    <svg viewBox="0 0 18 17"><rect width="18" height="17" fill="var(--red)"/><rect x="4" y="5" width="10" height="7" fill="none" stroke="#fff" stroke-width="1"/><path d="M4 5l5 4 5-4" fill="none" stroke="#fff" stroke-width="1"/></svg>contact@ironleaftraining.com</div>
  <div class="contact" style="top:770px">
    <svg viewBox="0 0 18 17"><rect width="18" height="17" fill="var(--red)"/><circle cx="9" cy="8.5" r="5" fill="none" stroke="#fff" stroke-width="1"/><ellipse cx="9" cy="8.5" rx="2.2" ry="5" fill="none" stroke="#fff" stroke-width="1"/><path d="M4 8.5h10" stroke="#fff" stroke-width="1"/></svg>www.ironleaftraining.com</div>
</section>

<!-- BACK -->
<section class="card card--back">
  <svg class="art" viewBox="0 0 360 360" role="img" aria-label="Photo of an athlete working with red battle ropes in a dark gym">
    <defs>
      <linearGradient id="gymDark" x1="0" y1="0" x2="1" y2="1">
        <stop offset="0" stop-color="var(--photo-dark-2)"/>
        <stop offset=".55" stop-color="var(--photo-dark-1)"/>
        <stop offset="1" stop-color="var(--photo-dark-2)"/>
      </linearGradient>
    </defs>
    <polygon points="0,0 360,0 360,234 71,286 0,246" fill="url(#gymDark)"/>
    <polygon points="0,244 71,284 360,232 360,238 71,291 0,250" fill="var(--red)"/>
  </svg>

  <div class="brand">
    <div class="brand__name"><span class="brand__mark"></span>IRONLEAF</div>
    <div class="brand__tag">PRIVATE TRAINING STUDIO</div>
  </div>

  <h2 class="section-title">HOW DO YOU GET STARTED?</h2>
  <div class="rule" style="top:336px"></div>
  <p class="body-copy" style="top:348px;width:320px;font-size:10.9px;line-height:13.7px">We schedule prospective clients for a no cost or obligation consultation. At that consultation we will do a movement screen with you. This will allow the trainer to see what level of flexibility and strength you are currently at. You will be able to discuss your goals and other issues (injuries, etc) at that time.</p>

  <div class="band" style="top:466px;height:233px"></div>
  <div class="tag" style="top:454px">Our Rates -</div>

  <ul class="rates">
    <li class="lead">All Sessions are 60 minutes</li>
    <li><span class="when">1 time per week</span>[ $110 per session ]</li>
    <li><span class="when">2 times per week</span>[ $85 per session ]</li>
    <li><span class="when">3 times per week</span>[ $80 per session ]</li>
  </ul>

  <div class="partner">Add $40 for a Partnered Session</div>

  <div class="example">
    <div class="lead">Example :</div>
    <div class="row"><span>A Partnered Session</span><span>[ 2 people training together ]</span></div>
    <div class="row"><span>coming twice a week is</span><span>[ $125 per session ]</span></div>
  </div>

  <div class="contact-line"></div>
  <div class="contact-tag">CONTACT US</div>
  <div class="contact contact--phone" style="top:724px">
    <svg viewBox="0 0 18 17"><rect width="18" height="17" fill="var(--red)"/><path d="M5 4l2.5-.5 1 2.5-1.3 1a6 6 0 0 0 3 3l1-1.3 2.5 1-.5 2.5C9 12.5 5.5 9 5 4z" fill="none" stroke="#fff" stroke-width="1"/></svg>555.014.2290</div>
  <div class="contact" style="top:747px">
    <svg viewBox="0 0 18 17"><rect width="18" height="17" fill="var(--red)"/><rect x="4" y="5" width="10" height="7" fill="none" stroke="#fff" stroke-width="1"/><path d="M4 5l5 4 5-4" fill="none" stroke="#fff" stroke-width="1"/></svg>contact@ironleaftraining.com</div>
  <div class="contact" style="top:770px">
    <svg viewBox="0 0 18 17"><rect width="18" height="17" fill="var(--red)"/><circle cx="9" cy="8.5" r="5" fill="none" stroke="#fff" stroke-width="1"/><ellipse cx="9" cy="8.5" rx="2.2" ry="5" fill="none" stroke="#fff" stroke-width="1"/><path d="M4 8.5h10" stroke="#fff" stroke-width="1"/></svg>www.ironleaftraining.com</div>
</section>

</body>
</html>
```